VnR Life Sciences is a Company providing consultancy services to companies operating within the Life Sciences Industry; namely pharmaceutical and Medical Devices. VnR stands for Vision and Reach; since we mainly provide Quality related consultancy but our approach is to help companies Grow. Thus Business Development is another area we focus on.
We do have the logos for our company now we are lookign for a professional slide deck to use for our ppts.

```html
<!DOCTYPE html>
<html lang="en">
<head>
<meta charset="utf-8">
<title>VnR Life Sciences – Slide Deck</title>
<link rel="stylesheet" href="https://fonts.googleapis.com/css2?family=Manrope:wght@300;400;500;600;700;800&display=swap">
<style>
:root{
  --stage:#353535;
  --gold:#e8b22e;
  --gold-pale:#f8ecce;
  --cream:#fdf6e4;
  --ink:#151515;
  --body:#3a3a3a;
  --muted:#6b6b6b;
  --forest:#0f2f2d;
  --grey-slide:#e8e8e8;
  --white:#ffffff;
}
*{margin:0;padding:0;box-sizing:border-box}
html,body{width:1039px;height:1200px;overflow:hidden;background:var(--stage)}
body{font-family:"Manrope",sans-serif;color:var(--ink);position:relative}
.slide{position:absolute;width:453px;height:255px;background:var(--white);overflow:hidden}
.col-a{left:57px}.col-b{left:541px}
.row-1{top:54px}.row-2{top:331px}.row-3{top:611px}.row-4{top:892px}
.abs{position:absolute}
.mark{position:absolute;background:var(--gold);border-radius:3px}
.brand{position:absolute;text-align:center;white-space:nowrap;transform:translateX(-50%)}
.brand-name{font-size:8px;font-weight:600;color:var(--ink);letter-spacing:0}
.brand-tag{font-size:4.2px;font-weight:400;color:var(--muted);letter-spacing:0}
.photo{position:absolute}
p{color:var(--body)}
.small{font-size:5.6px;line-height:7.6px}
.justify{text-align:justify}

/* Cover */
.cover .welcome{left:0;width:100%;top:154px;text-align:center;font-size:19px;font-weight:400}
.cover .headline{left:0;width:100%;top:186px;text-align:center;font-size:26px;font-weight:500;color:var(--gold)}

/* Agenda */
.agenda-panel{left:0;top:0;width:198px;height:255px;background:var(--gold)}
.agenda-title{left:0;width:182px;top:155px;text-align:center;font-size:26px;font-weight:800;color:var(--white);letter-spacing:.5px}
.agenda-item{position:absolute;left:189px}
.agenda-num{position:absolute;left:0;top:0;width:18px;height:18px;border-radius:50%;background:var(--gold);color:var(--white);font-size:6px;font-weight:700;display:flex;align-items:center;justify-content:center;border:2px solid var(--white)}
.agenda-item h4{position:absolute;left:28px;top:-8px;font-size:7.5px;font-weight:700;white-space:nowrap}
.agenda-item p{position:absolute;left:28px;top:2px;font-size:5.8px;white-space:nowrap}

/* About */
.about h2{left:19px;top:76px;font-size:14.5px;font-weight:700}
.about .copy{left:19px;top:100px;width:187px}
.about .copy p+p{margin-top:6px}
.band-gold{left:286px;top:0;width:81px;height:255px;background:var(--gold)}
.band-pale{left:373px;top:0;width:80px;height:255px;background:var(--gold-pale)}

/* Section headers */
.rule{position:absolute;width:2.5px;background:var(--gold)}
.sec-title{position:absolute;font-size:17px;font-weight:400}
.services .lower{left:0;top:68px;width:453px;height:187px;background:var(--forest)}
.card{position:absolute;top:92px;width:82px}
.card .icon{width:34px;height:34px;background:var(--gold);border-radius:3px;display:flex;align-items:center;justify-content:center}
.card h3{margin-top:16px;font-size:10px;font-weight:400;color:var(--white)}
.card p{margin-top:6px;font-size:5.6px;line-height:7.5px;color:#e6ece9}

/* Feature list */
.feature{background:var(--grey-slide)}
.feature h2{left:19px;top:74px;font-size:17.5px;font-weight:400;line-height:20px;width:260px}
.bullet{position:absolute;left:25px;width:195px}
.bullet::before{content:"";position:absolute;left:0;top:2px;width:6px;height:6px;border-radius:50%;background:var(--gold)}
.bullet p{margin-left:14px;font-size:5.6px;line-height:7.6px}

/* Process */
.step{position:absolute;left:19px;width:180px}
.step h4{font-size:7.5px;font-weight:700}
.step p{margin-top:2px;font-size:5.6px;line-height:7.5px}
.divider{position:absolute;left:0;width:198px;height:.6px;background:#d7cdb6}
.node{position:absolute;width:24px;height:24px;background:var(--gold);border-radius:4px;display:flex;align-items:center;justify-content:center;transform:translate(-50%,-50%)}

/* Closing */
.thanks{left:0;width:100%;top:155px;text-align:center;font-size:32px;font-weight:800;color:var(--gold);letter-spacing:-.5px}
.foot-band{left:0;bottom:0;width:100%;height:6px;background:var(--gold)}
</style>
</head>
<body>

<!-- Cover -->
<section class="slide cover col-a row-1">
  <div class="photo" style="right:0;top:0;width:110px;height:90px;background:radial-gradient(ellipse at 80% 20%,rgba(232,178,46,.35),rgba(255,255,255,0) 70%)" role="img" aria-label="Gold molecular hexagon pattern"></div>
  <div class="photo" style="left:0;bottom:0;width:70px;height:90px;background:radial-gradient(ellipse at 20% 80%,rgba(232,178,46,.35),rgba(255,255,255,0) 70%)" role="img" aria-label="Gold molecular hexagon pattern"></div>
  <div class="mark" style="left:210px;top:39px;width:33px;height:33px"></div>
  <div class="brand brand-name" style="left:227px;top:88px;font-size:11px">VnR Life Sciences</div>
  <div class="brand brand-tag" style="left:227px;top:106px;font-size:5px">Quality and business development consultancy</div>
  <div class="abs welcome">Welcome to</div>
  <div class="abs headline">VnR lifesciences</div>
</section>

<!-- Agenda -->
<section class="slide agenda col-b row-1">
  <div class="abs agenda-panel"></div>
  <div class="mark" style="left:54px;top:62px;width:77px;height:77px;background:var(--white);border-radius:6px"></div>
  <div class="abs agenda-title">AGENDA</div>
  <div class="agenda-item" style="top:18px"><span class="agenda-num">01</span><h4>SLIDE 1</h4><p>Lorem Ipsum is simply dummy text of the printing</p></div>
  <div class="agenda-item" style="top:50px"><span class="agenda-num">02</span><h4>SLIDE 2</h4><p>Sed ut perspiciatis unde omnis</p></div>
  <div class="agenda-item" style="top:83px"><span class="agenda-num">03</span><h4>SLIDE 3</h4><p>At vero eos et accusamus et iusto odio dignissimos</p></div>
  <div class="agenda-item" style="top:115px"><span class="agenda-num">04</span><h4>SLIDE 4</h4><p>These cases are perfectly simple</p></div>
  <div class="agenda-item" style="top:149px"><span class="agenda-num">05</span><h4>SLIDE 5</h4><p>Nemo enim ipsam voluptatem quia voluptas</p></div>
  <div class="agenda-item" style="top:181px"><span class="agenda-num">06</span><h4>SLIDE 6</h4><p>Duis aute irure dolor in reprehenderit in voluptate velit</p></div>
  <div class="agenda-item" style="top:218px"><span class="agenda-num">07</span><h4>SLIDE 7</h4><p>Lorem Ipsum is simply dummy text of the printing</p></div>
</section>

<!-- About -->
<section class="slide about col-a row-2">
  <div class="abs band-gold"></div>
  <div class="abs band-pale"></div>
  <div class="mark" style="left:105px;top:15px;width:20px;height:20px"></div>
  <div class="brand brand-name" style="left:115px;top:44px">VnR Life Sciences</div>
  <div class="brand brand-tag" style="left:115px;top:57px">Quality and business development consultancy</div>
  <h2 class="abs">About US</h2>
  <div class="abs copy small justify">
    <p>Sed ut perspiciatis unde omnis iste natus error sit voluptatem accusantium doloremque laudantium, totam rem aperiam, eaque ipsa quae ab illo inventore veritatis et quasi architecto beatae vitae dicta sunt explicabo. Nemo enim ipsam voluptatem quia voluptas sit aspernatur aut odit aut fugit, sed quia consequuntur magni dolores eos qui ratione voluptatem sequi nesciunt. Neque porro quisquam est, qui dolorem ipsum quia dolor sit amet, consectetur, adipisci velit, sed quia non numquam eius modi tempora incidunt ut labore et dolore magnam aliquam quaerat voluptatem. Ut enim ad minima veniam, quis nostrum exercitationem ullam corporis suscipit laboriosam, nisi ut aliquid ex ea commodi consequatu</p>
    <p>Ut enim ad minima veniam, quis nostrum exercitationem ullam corporis suscipit laboriosam, nisi ut aliquid ex ea commodi consequatu Quis autem vel eum iure reprehenderit qui in ea voluptate ve</p>
  </div>
  <div class="photo" style="left:250px;top:0;width:91px;height:56px;background:linear-gradient(135deg,#0b2a4a,#2f7fb0 55%,#d86a2c)" role="img" aria-label="Glowing capsules in a blue laboratory light"></div>
  <div class="photo" style="left:238px;top:64px;width:209px;height:148px;background:linear-gradient(120deg,#d7e6f3,#7fa7cc 50%,#3c6690)" role="img" aria-label="Scientist in protective suit working on a production line"></div>
  <div class="photo" style="left:231px;top:171px;width:91px;height:75px;background:var(--white)"></div>
  <div class="photo" style="left:233px;top:173px;width:87px;height:71px;background:linear-gradient(160deg,#3a4a5a,#c9ccce 60%,#eeeae2)" role="img" aria-label="Medical monitoring equipment"></div>
</section>

<!-- Services -->
<section class="slide services col-b row-2">
  <div class="mark" style="left:98px;top:9px;width:20px;height:20px"></div>
  <div class="brand brand-name" style="left:108px;top:38px">VnR Life Sciences</div>
  <div class="brand brand-tag" style="left:108px;top:51px">Quality and business development consultancy</div>
  <div class="rule" style="left:226px;top:13px;height:45px"></div>
  <div class="sec-title" style="left:242px;top:11px">Services</div>
  <p class="abs small" style="left:242px;top:37px;width:180px">Lorem ipsum dolor sit amet, consectetur adipiscing elit, sed do eiusmod tempor incididunt ut labore</p>
  <div class="abs lower"></div>
  <div class="card" style="left:15px">
    <div class="icon"><svg width="20" height="20" viewBox="0 0 20 20" fill="none" stroke="#15211f" stroke-width="1.6"><rect x="5" y="2" width="11" height="14" rx="1"/><path d="M8 6h5M8 9h5M8 12h3"/></svg></div>
    <h3>Lorem Ipsum</h3>
    <p>Sed ut perspiciatis unde omnis iste natus error sit voluptatem accusantium dolore mque laudantium, totam rem aperiam, eaque ipsa quae ab illo inventore veritatis et quasi architecto beatae vitae dicta sunt explicabo. Nemo enim ipsam voluptatem</p>
  </div>
  <div class="card" style="left:125px">
    <div class="icon"><svg width="20" height="20" viewBox="0 0 20 20" fill="#15211f" stroke="#15211f" stroke-width="1.2"><circle cx="10" cy="10" r="2.5"/><circle cx="4" cy="4" r="2"/><circle cx="16" cy="4" r="2"/><circle cx="4" cy="16" r="2"/><circle cx="16" cy="16" r="2"/><path d="M4 4l12 12M16 4L4 16"/></svg></div>
    <h3>Lorem Ipsum</h3>
    <p>Sed ut perspiciatis unde omnis iste natus error sit voluptatem accusantium dolore mque laudantium, totam rem aperiam, eaque ipsa quae ab illo inventore veritatis et quasi architecto beatae vitae dicta sunt explicabo. Nemo enim ipsam voluptatem</p>
  </div>
  <div class="card" style="left:244px">
    <div class="icon"><svg width="20" height="20" viewBox="0 0 20 20" fill="none" stroke="#15211f" stroke-width="1.6"><rect x="4" y="2" width="12" height="16" rx="1"/><path d="M7 9h6M7 12h6M7 15h4"/></svg></div>
    <h3>Lorem Ipsum</h3>
    <p>Sed ut perspiciatis unde omnis iste natus error sit voluptatem accusantium dolore mque laudantium, totam rem aperiam, eaque ipsa quae ab illo inventore veritatis et quasi architecto beatae vitae dicta sunt explicabo. Nemo enim ipsam voluptatem</p>
  </div>
  <div class="card" style="left:358px">
    <div class="icon"><svg width="22" height="20" viewBox="0 0 22 20" fill="none" stroke="#15211f" stroke-width="1.4"><path d="M4 10l3-2 3 2v4l-3 2-3-2zM10 10l3-2 3 2v4l-3 2-3-2zM16 10l3-2 3 2v4l-3 2-3-2z"/><circle cx="9" cy="4" r="2.5" fill="#15211f"/></svg></div>
    <h3>Lorem Ipsum</h3>
    <p>Sed ut perspiciatis unde omnis iste natus error sit voluptatem accusantium dolore mque laudantium, totam rem aperiam, eaque ipsa quae ab illo inventore veritatis et quasi architecto beatae vitae dicta sunt explicabo. Nemo enim ipsam voluptatem</p>
  </div>
</section>

<!-- Feature list -->
<section class="slide feature col-a row-3">
  <div class="photo" style="left:300px;top:0;width:153px;height:255px;background:linear-gradient(100deg,rgba(232,232,232,1),rgba(240,242,245,1) 25%,#9fd0ec 55%,#2f97d6 75%,#f0f0f0)" role="img" aria-label="Blue, orange and white pills scattered on a white surface"></div>
  <div class="mark" style="left:103px;top:17px;width:20px;height:20px"></div>
  <div class="brand brand-name" style="left:113px;top:46px">VnR Life Sciences</div>
  <div class="brand brand-tag" style="left:113px;top:59px">Quality and business development consultancy</div>
  <h2 class="abs">Sed ut perspiciatis unde omnis iste natus error sit voluptatem</h2>
  <div class="bullet" style="top:131px"><p>Lorem ipsum dolor sit amet, consectetur adipiscing elit, sed do eiusmod tempor incididunt ut labore</p></div>
  <div class="bullet" style="top:153px"><p>Lorem ipsum dolor sit amet, consectetur adipiscing elit, sed do eiusmod tempor incididunt ut labore</p></div>
  <div class="bullet" style="top:176px"><p>Lorem ipsum dolor sit amet, consectetur adipiscing elit, sed do eiusmod tempor incididunt ut labore</p></div>
  <div class="bullet" style="top:198px"><p>Lorem ipsum dolor sit amet, consectetur adipiscing elit, sed do eiusmod tempor incididunt ut labore</p></div>
  <div class="bullet" style="top:222px"><p>Lorem ipsum dolor sit amet, consectetur adipiscing elit, sed do eiusmod tempor incididunt ut labore</p></div>
</section>

<!-- Process -->
<section class="slide process col-b row-3">
  <svg class="abs" style="left:0;top:0" width="453" height="255" viewBox="0 0 453 255"><path d="M0 0H297C250 50 222 120 236 175C246 215 280 240 311 255H0Z" fill="var(--cream)"/></svg>
  <div class="step" style="top:16px"><h4>LOREM IPSUM</h4><p>Lorem ipsum dolor sit amet, consectetur adipiscing elit, sed do eiusmod tempor incididunt ut labore</p></div>
  <div class="divider" style="top:51px"></div>
  <div class="step" style="top:58px"><h4>LOREM IPSUM</h4><p>Lorem ipsum dolor sit amet, consectetur adipiscing elit, sed do eiusmod tempor incididunt ut labore</p></div>
  <div class="divider" style="top:96px"></div>
  <div class="step" style="top:107px"><h4>LOREM IPSUM</h4><p>Lorem ipsum dolor sit amet, consectetur adipiscing elit, sed do eiusmod tempor incididunt ut labore</p></div>
  <div class="divider" style="top:145px"></div>
  <div class="step" style="top:159px"><h4>LOREM IPSUM</h4><p>Lorem ipsum dolor sit amet, consectetur adipiscing elit, sed do eiusmod tempor incididunt ut labore</p></div>
  <div class="divider" style="top:198px"></div>
  <div class="step" style="top:207px"><h4>LOREM IPSUM</h4><p>Lorem ipsum dolor sit amet, consectetur adipiscing elit, sed do eiusmod tempor incididunt ut labore</p></div>
  <div class="node" style="left:268px;top:26px"><svg width="12" height="13" viewBox="0 0 12 13" fill="none" stroke="#222" stroke-width="1.2"><path d="M2 1h5l3 3v8H2z"/><path d="M4 7h4M4 9.5h4"/></svg></div>
  <div class="node" style="left:242px;top:68px"><svg width="12" height="12" viewBox="0 0 12 12" fill="none" stroke="#222" stroke-width="1.2"><path d="M4 1h4M5 1v4L2 11h8L7 5V1"/></svg></div>
  <div class="node" style="left:225px;top:122px"><svg width="12" height="12" viewBox="0 0 12 12" fill="none" stroke="#222" stroke-width="1.2"><rect x="2" y="1" width="8" height="10"/><path d="M4 4v5M6 4v5M8 4v5"/></svg></div>
  <div class="node" style="left:235px;top:173px"><svg width="12" height="12" viewBox="0 0 12 12" fill="none" stroke="#222" stroke-width="1.2"><rect x="1" y="2" width="10" height="7"/><path d="M4 11h4"/></svg></div>
  <div class="node" style="left:263px;top:220px"><svg width="12" height="12" viewBox="0 0 12 12" fill="none" stroke="#222" stroke-width="1.2"><rect x="2" y="1" width="8" height="10" rx="1"/><circle cx="6" cy="5" r="1.5"/></svg></div>
  <div class="mark" style="left:333px;top:97px;width:20px;height:20px"></div>
  <div class="brand brand-name" style="left:344px;top:126px">VnR Life Sciences</div>
  <div class="brand brand-tag" style="left:344px;top:139px">Quality and business development consultancy</div>
</section>

<!-- Solutions -->
<section class="slide solutions col-a row-4">
  <div class="mark" style="left:97px;top:13px;width:20px;height:20px"></div>
  <div class="brand brand-name" style="left:107px;top:42px">VnR Life Sciences</div>
  <div class="brand brand-tag" style="left:107px;top:55px">Quality and business development consultancy</div>
  <div class="rule" style="left:226px;top:16px;height:45px"></div>
  <div class="sec-title" style="left:245px;top:14px">Solutions</div>
  <p class="abs small" style="left:245px;top:41px;width:180px">Lorem ipsum dolor sit amet, consectetur adipiscing elit, sed do eiusmod tempor incididunt ut labore</p>
  <div class="photo" style="left:10px;top:75px;width:219px;height:166px;border-radius:5px;background:radial-gradient(circle at 45% 40%,#d8f4ff,#6ccdf0 35%,#1d6d9a 75%,#0c3550)" role="img" aria-label="MRI scanner in a brightly lit clinical room"></div>
  <div class="abs small justify" style="left:245px;top:81px;width:188px">
    <p>At vero eos et accusamus et iusto odio dignissimos ducimus qui blanditiis praesentium voluptatum deleniti atque corrupti quos dolores et quas molestias excepturi sint occaecati cupiditate non provident, similique sunt in culpa qui officia deserunt mollitia animi, id est laborum et dolorum fuga. Et harum quidem rerum facilis est et expedita distinctio. Nam libero tempore, cum soluta nobis est eligendi optio cumque nihil impedit quo minus id quod maxime placeat facere possimus, omnis voluptas assumenda est, omnis dolor repellendus. Temporibus autem quibusdam et aut officiis debitis aut rerum necessitatibus saepe eveniet ut et voluptates repudiandae sint et molestiae non recusandae. Itaque earum rerum hic tenetur a sapiente delectus, ut aut reiciendis voluptatibus maiores alias consequatur aut perferendis doloribus asperiores repella</p>
    <p style="margin-top:6px">Temporibus autem quibusdam et aut officiis debitis aut rerum necessitatibus saepe eveniet ut et voluptates repudiandae sint et molestiae non recusandae. Itaque earum rerum hic tenetur a sapiente delectus, ut aut reiciendis voluptatibus maiores alias consequatur aut perferendis doloribus asperiores repella</p>
  </div>
</section>

<!-- Closing -->
<section class="slide closing col-b row-4">
  <div class="mark" style="left:211px;top:39px;width:35px;height:35px"></div>
  <div class="brand brand-name" style="left:228px;top:88px;font-size:12px">VnR Life Sciences</div>
  <div class="brand brand-tag" style="left:228px;top:108px;font-size:5.5px">Quality and business development consultancy</div>
  <div class="abs thanks">THANK YOU</div>
  <div class="abs foot-band"></div>
</section>

</body>
</html>
```